Business Card Design

The Velmora Companion Animal Foundation is a not-for-profit organization that provides the best quality care and rehabilitation for pets in need. All our guests are treated with dignity and respect in a loving atmosphere. We offer the training and rehabilitation needed to make the transition to a forever home smooth and effective. As a no-kill facility, we do a behavioral analysis of each of our guests and put together a plan to make sure they are ready for a forever home. Velmora means a place of great beauty, luxury, and contentment.
We are looking for a professional looking card, rather than cutesy, that makes people take us seriously as we need to raise significant funds to support our efforts. Would like the name of company used in a way to be logo-ish, so be creative there.

Target Market(s)

A wealthy, animal loving market.

Industry/Entity Type

Training

Contact Information for Business Card

Velmora Companion Animal Foundation
R. Glenn Ostrak, CEO
P.O. Box 4852, Fernhollow, OR 97999
www.velmorapetshelter.example
(555) 555-0178

```html
<!DOCTYPE html>
<html lang="en">
<head>
<meta charset="utf-8">
<title>Velmora Companion Animal Foundation – Business Card</title>
<link rel="stylesheet" href="https://fonts.googleapis.com/css2?family=Open+Sans:wght@400;600;700&display=swap">
<style>
  :root {
    --navy: #0f4a7e;
    --paper: #f3f4f6;
    --white: #ffffff;
    --backdrop: #e7e5e2;
  }
  * { box-sizing: border-box; margin: 0; padding: 0; }
  html, body { width: 1200px; height: 800px; overflow: hidden; }
  body {
    background: var(--backdrop);
    font-family: "Open Sans", Arial, sans-serif;
    position: relative;
  }
  .card {
    position: absolute;
    top: 245px;
    width: 540px;
    height: 309px;
    overflow: hidden;
    background: var(--navy);
    box-shadow: 0 6px 18px rgba(0,0,0,0.18);
  }
  .card--front { left: 40px; }
  .card--back { left: 620px; }

  /* shared logo lockup: one colour, one weight */
  .logo { display: flex; align-items: center; gap: 16px; color: var(--white); font-weight: 600; }
  .logo__mark { width: 14px; height: 14px; border-radius: 50%; background: var(--white); flex: none; }
  .logo__name { font-size: 30px; letter-spacing: 3px; line-height: 1; }
  .logo__sub { font-size: 14px; letter-spacing: 0.5px; line-height: 1.2; margin-top: 4px; }

  /* front */
  .front__header {
    position: absolute; left: 0; top: 0; right: 0; height: 84px;
    padding: 16px 30px 0 30px;
  }
  .front__band {
    position: absolute; left: 0; right: 0; top: 84px; height: 142px;
    background: var(--paper);
  }
  .front__footer {
    position: absolute; left: 0; right: 0; bottom: 0; height: 83px;
    display: flex; align-items: center; padding-left: 30px;
    color: var(--white); font-size: 14px; letter-spacing: 2.2px;
  }
  .person { position: absolute; left: 30px; top: 16px; color: var(--navy); }
  .person__name { font-size: 20px; font-weight: 700; letter-spacing: 0.5px; }
  .person__role { font-size: 13px; margin-top: 1px; }

  .contact { position: absolute; right: 34px; bottom: 18px; list-style: none; color: var(--navy); font-size: 15px; }
  .contact li { display: flex; align-items: center; gap: 8px; line-height: 1.55; }
  .contact svg { width: 15px; height: 15px; flex: none; }

  /* back */
  .back__logo {
    position: absolute; left: 0; right: 0; top: 96px;
    display: flex; justify-content: center;
  }
  .back__logo .logo__name { font-size: 40px; letter-spacing: 4px; }
  .back__logo .logo__sub { font-size: 17px; }
  .back__logo .logo__mark { width: 18px; height: 18px; }
  .back__web {
    position: absolute; left: 0; right: 0; bottom: 34px; text-align: center;
    color: var(--white); font-size: 13px; letter-spacing: 2.4px;
  }
</style>
</head>
<body>

  <section class="card card--front" aria-label="Business card front">
    <header class="front__header">
      <div class="logo">
        <div>
          <div class="logo__name">VELMORA</div>
          <div class="logo__sub">COMPANION ANIMAL FOUNDATION</div>
        </div>
        <span class="logo__mark"></span>
      </div>
    </header>

    <div class="front__band">
      <div class="person">
        <div class="person__name">R. GLENN OSTRAK</div>
        <div class="person__role">CEO</div>
      </div>
      <ul class="contact">
        <li>
          <svg viewBox="0 0 16 16" aria-hidden="true"><rect width="16" height="16" rx="3" fill="var(--navy)"/><path d="M5 3.5l1.6 2.3-1 1c.6 1.3 1.6 2.3 2.9 2.9l1-1 2.3 1.6-.8 1.8C7.3 12 4 8.7 3.2 4.3z" fill="var(--white)"/></svg>
          (555) 555-0178
        </li>
        <li>
          <svg viewBox="0 0 16 16" aria-hidden="true"><rect width="16" height="16" rx="3" fill="var(--navy)"/><circle cx="8" cy="8" r="4.8" fill="none" stroke="var(--white)" stroke-width="1.1"/><path d="M3.2 8h9.6M8 3.2c-2 2.6-2 7 0 9.6M8 3.2c2 2.6 2 7 0 9.6" fill="none" stroke="var(--white)" stroke-width="1"/></svg>
          www.velmorapetshelter.example
        </li>
      </ul>
    </div>

    <footer class="front__footer">P.O. Box 4852, Fernhollow, OR 97999</footer>
  </section>

  <section class="card card--back" aria-label="Business card back">
    <div class="back__logo">
      <div class="logo">
        <div>
          <div class="logo__name">VELMORA</div>
          <div class="logo__sub">COMPANION ANIMAL FOUNDATION</div>
        </div>
        <span class="logo__mark"></span>
      </div>
    </div>
    <div class="back__web">www.velmorapetshelter.example</div>
  </section>

</body>
</html>
```